Stationery and Business Card Design

We need stationary design for our new company pelvanta. Pelvanta is a company that provides city apartment rentals for tourists in Athens We need business cards, letterheads for A4 and A5 and envelopes for A4 A5. The design needs to be modern, friendly and corporate.

Target Market(s)

City Tourists

Industry/Entity Type

Tourism

```html
<!DOCTYPE html>
<html lang="en">
<head>
<meta charset="utf-8">
<title>Pelvanta Stationery</title>
<link href="https://fonts.googleapis.com/css2?family=Open+Sans:wght@400;600&family=Roboto+Condensed:wght@400&display=swap" rel="stylesheet">
<style>
  :root {
    --plum: #920252;
    --graphite: #3d3d3d;
    --backdrop: #e8e7e7;
    --paper: #ffffff;
    --ink: #444444;
    --rule: #cfcfcf;
  }
  * { box-sizing: border-box; margin: 0; padding: 0; }
  html, body { width: 1200px; height: 965px; overflow: hidden; }
  body {
    background: var(--backdrop);
    font-family: "Open Sans", sans-serif;
    color: var(--ink);
    position: relative;
  }
  .icon-defs { position: absolute; width: 0; height: 0; }

  .sheet {
    position: absolute;
    background: linear-gradient(160deg, #ffffff 0%, #f7f7f7 60%, #efefef 100%);
    box-shadow: 0 2px 6px rgba(0,0,0,.18);
    overflow: hidden;
  }

  /* brand lockup */
  .brand { display: flex; flex-direction: column; align-items: center; }
  .brand-square { width: 3.8em; height: 3.8em; background: var(--plum); margin-bottom: .5em; }
  .brand-name { font-weight: 400; font-size: 2.7em; color: var(--plum); line-height: 1; letter-spacing: -.01em; }

  /* contact line */
  .contact-row {
    position: absolute; left: 0; right: 0;
    display: flex; justify-content: space-between; align-items: center;
    padding: 0 2em; font-size: 1em; white-space: nowrap;
  }
  .contact-item { display: flex; align-items: center; gap: .6em; }
  .contact-item + .contact-item { border-left: 1px solid var(--rule); padding-left: 1.2em; }
  .contact-item svg { width: 1em; height: 1em; fill: var(--plum); flex: none; }

  /* footer band */
  .band {
    position: absolute; left: 0; right: 0; bottom: 0; height: 1.9em;
    background: linear-gradient(120deg, var(--plum) 0 71%, var(--paper) 71% 72%, var(--graphite) 72% 100%);
  }

  /* letterheads */
  .letterhead-a4 { left: 110px; top: 80px; width: 420px; height: 600px; font-size: 9px; }
  .letterhead-a5 { left: 300px; top: 230px; width: 300px; height: 420px; font-size: 6.5px; }
  .letterhead-a4 .brand, .letterhead-a5 .brand { margin-top: 4.5em; }
  .letterhead-a4 .contact-row, .letterhead-a5 .contact-row { bottom: 3.3em; }
  .letterhead-a5 .contact-row { font-size: 5px; padding: 0 2.4em; bottom: 4.2em; }
  .letterhead-a5 .contact-item { gap: .5em; }
  .letterhead-a5 .contact-item + .contact-item { padding-left: .9em; }

  /* envelopes */
  .envelope { background: none; box-shadow: none; overflow: visible; }
  .envelope-flap { position: absolute; left: 0; top: 0; width: 100%; height: 60px; }
  .flap-name {
    position: absolute; left: 0; right: 0; top: 18px; text-align: center;
    color: var(--paper); font-size: 16px; transform: rotate(180deg);
  }
  .envelope-body {
    position: absolute; left: 0; right: 0; top: 60px; bottom: 0;
    background: linear-gradient(160deg, #ffffff 0%, #f6f6f6 70%, #eeeeee 100%);
    box-shadow: 0 2px 6px rgba(0,0,0,.18);
  }
  .envelope .brand { position: absolute; left: 1.9em; top: 1.9em; }
  .envelope .contact-row { bottom: 2.9em; }
  .envelope-dl { left: 637px; top: 68px; width: 430px; height: 275px; font-size: 7.2px; }
  .envelope-c5 { left: 638px; top: 359px; width: 430px; height: 360px; font-size: 7.2px; }
  .envelope-c5 .brand { font-size: 9.6px; top: 1.8em; left: 2em; }

  /* business cards */
  .card { top: 756px; width: 290px; height: 166px; font-size: 8px; }
  .card .band { height: 1.9em; }
  .card-front { left: 300px; }
  .card-front .brand { position: absolute; left: 0; right: 0; top: 4.2em; font-size: 9.5px; }
  .card-back { left: 631px; }
  .card-back .brand { position: absolute; left: 2.4em; top: 6.8em; font-size: 7.6px; }
  .card-divider { position: absolute; left: 146px; top: 24px; height: 88px; border-left: 1px solid var(--rule); }
  .card-details { position: absolute; left: 167px; top: 31px; }
  .person-name { font-family: "Roboto Condensed", sans-serif; font-size: 12px; color: #333; }
  .person-role { font-size: 7.5px; color: var(--plum); margin-bottom: 1.6em; }
  .card-details .contact-item { font-size: 6.4px; gap: .8em; margin-bottom: .6em; }
  .card-details .contact-item + .contact-item { border: 0; padding: 0; }
  .card-details .contact-gap { margin-top: 1.6em; }
</style>
</head>
<body>

<svg class="icon-defs" aria-hidden="true">
  <symbol id="icon-phone" viewBox="0 0 24 24"><path d="M6.6 10.8c1.4 2.8 3.8 5.1 6.6 6.6l2.2-2.2c.3-.3.7-.4 1-.2 1.1.4 2.3.6 3.6.6.6 0 1 .4 1 1V20c0 .6-.4 1-1 1C10.6 21 3 13.4 3 4c0-.6.4-1 1-1h3.5c.6 0 1 .4 1 1 0 1.3.2 2.5.6 3.6.1.3 0 .7-.2 1z"/></symbol>
  <symbol id="icon-pin" viewBox="0 0 24 24"><path d="M12 2C8.1 2 5 5.1 5 9c0 5.2 7 13 7 13s7-7.8 7-13c0-3.9-3.1-7-7-7zm0 9.5a2.5 2.5 0 1 1 0-5 2.5 2.5 0 0 1 0 5z"/></symbol>
  <symbol id="icon-mail" viewBox="0 0 24 24"><path d="M3 9l9-6 9 6v11H3V9zm2 1.2V18h14v-7.8l-7 4.6-7-4.6z"/></symbol>
  <symbol id="icon-globe" viewBox="0 0 24 24"><path d="M12 2a10 10 0 1 0 0 20 10 10 0 0 0 0-20zm6.9 6h-2.9a15 15 0 0 0-1.4-3.6A8 8 0 0 1 18.9 8zM12 4c.8 1.2 1.5 2.5 1.9 4h-3.8c.4-1.5 1.1-2.8 1.9-4zM4.3 14a8 8 0 0 1 0-4h3.4a16 16 0 0 0 0 4H4.3zm.8 2h2.9c.3 1.3.8 2.5 1.4 3.6A8 8 0 0 1 5.1 16zM8 8H5.1a8 8 0 0 1 4.3-3.6C8.8 5.5 8.3 6.7 8 8zm4 12c-.8-1.2-1.5-2.5-1.9-4h3.8c-.4 1.5-1.1 2.8-1.9 4zm2.3-6H9.7a14 14 0 0 1 0-4h4.6a14 14 0 0 1 0 4zm.3 5.6c.6-1.1 1.1-2.3 1.4-3.6h2.9a8 8 0 0 1-4.3 3.6zM16.3 14a16 16 0 0 0 0-4h3.4a8 8 0 0 1 0 4h-3.4z"/></symbol>
</svg>

<!-- A4 letterhead -->
<section class="sheet letterhead-a4">
  <div class="brand"><div class="brand-square"></div><div class="brand-name">Pelvanta</div></div>
  <div class="contact-row">
    <span class="contact-item"><svg><use href="#icon-phone"/></svg>0210 448 915</span>
    <span class="contact-item"><svg><use href="#icon-pin"/></svg>12 Irida Street, Plaka, Athens</span>
    <span class="contact-item"><svg><use href="#icon-mail"/></svg>daria@pelvanta.com</span>
  </div>
  <div class="band"></div>
</section>

<!-- A5 letterhead -->
<section class="sheet letterhead-a5">
  <div class="brand"><div class="brand-square"></div><div class="brand-name">Pelvanta</div></div>
  <div class="contact-row">
    <span class="contact-item"><svg><use href="#icon-phone"/></svg>0210 448 915</span>
    <span class="contact-item"><svg><use href="#icon-pin"/></svg>12 Irida Street, Plaka, Athens</span>
    <span class="contact-item"><svg><use href="#icon-mail"/></svg>daria@pelvanta.com</span>
    <span class="contact-item"><svg><use href="#icon-globe"/></svg>www.pelvanta.com</span>
  </div>
  <div class="band"></div>
</section>

<!-- DL envelope -->
<section class="sheet envelope envelope-dl">
  <svg class="envelope-flap" viewBox="0 0 430 60" preserveAspectRatio="none" aria-hidden="true">
    <path d="M0 60 L14 8 Q16 0 26 0 L404 0 Q414 0 416 8 L430 60 Z" fill="var(--plum)"/>
  </svg>
  <div class="flap-name">Pelvanta</div>
  <div class="envelope-body">
    <div class="brand"><div class="brand-square"></div><div class="brand-name">Pelvanta</div></div>
    <div class="contact-row">
      <span class="contact-item"><svg><use href="#icon-phone"/></svg>0210 448 915</span>
      <span class="contact-item"><svg><use href="#icon-pin"/></svg>12 Irida Street, Plaka, Athens</span>
      <span class="contact-item"><svg><use href="#icon-mail"/></svg>daria@pelvanta.com</span>
      <span class="contact-item"><svg><use href="#icon-globe"/></svg>www.pelvanta.com</span>
    </div>
    <div class="band"></div>
  </div>
</section>

<!-- C5 envelope -->
<section class="sheet envelope envelope-c5">
  <svg class="envelope-flap" viewBox="0 0 430 60" preserveAspectRatio="none" aria-hidden="true">
    <path d="M0 60 L14 8 Q16 0 26 0 L404 0 Q414 0 416 8 L430 60 Z" fill="var(--plum)"/>
  </svg>
  <div class="flap-name">Pelvanta</div>
  <div class="envelope-body">
    <div class="brand"><div class="brand-square"></div><div class="brand-name">Pelvanta</div></div>
    <div class="contact-row">
      <span class="contact-item"><svg><use href="#icon-phone"/></svg>0210 448 915</span>
      <span class="contact-item"><svg><use href="#icon-pin"/></svg>12 Irida Street, Plaka, Athens</span>
      <span class="contact-item"><svg><use href="#icon-mail"/></svg>daria@pelvanta.com</span>
      <span class="contact-item"><svg><use href="#icon-globe"/></svg>www.pelvanta.com</span>
    </div>
    <div class="band"></div>
  </div>
</section>

<!-- Business card front -->
<section class="sheet card card-front">
  <div class="brand"><div class="brand-square"></div><div class="brand-name">Pelvanta</div></div>
  <div class="band"></div>
</section>

<!-- Business card back -->
<section class="sheet card card-back">
  <div class="brand"><div class="brand-square"></div><div class="brand-name">Pelvanta</div></div>
  <div class="card-divider"></div>
  <div class="card-details">
    <div class="person-name">Daria Lenos</div>
    <div class="person-role">Managing Director</div>
    <div class="contact-item"><svg><use href="#icon-phone"/></svg>0210 448 915</div>
    <div class="contact-item"><svg><use href="#icon-pin"/></svg>12 Irida Street, Plaka, Athens</div>
    <div class="contact-item contact-gap"><svg><use href="#icon-mail"/></svg>daria@pelvanta.com</div>
    <div class="contact-item"><svg><use href="#icon-globe"/></svg>www.pelvanta.com</div>
  </div>
  <div class="band"></div>
</section>

</body>
</html>
```